Melissa Dorvan Personal Business Card

I like orange. It's would better if my card have an orange background
Address: 5820 Halvers Lane #417
San Jose
California
US
Tel: 4085172049

Industry/Entity Type

Business

```html
<!DOCTYPE html>
<html lang="en">
<head>
<meta charset="utf-8">
<title>Melissa Dorvan – Business Card</title>
<link href="https://fonts.googleapis.com/css2?family=Exo+2:wght@400;500;700&display=swap" rel="stylesheet">
<style>
  :root {
    --stage: #2b2725;
    --card: #f4f4f4;
    --card-edge: #e2e2e2;
    --ink: #2a2a2a;
    --ink-soft: #3a3a3a;
    --orange: #f28a1e;
    --orange-deep: #e0650f;
    --orange-light: #ffc07a;
    --rule: #1c1c1c;
  }
  * { margin: 0; padding: 0; box-sizing: border-box; }
  html, body { width: 1200px; height: 900px; overflow: hidden; }
  body {
    background: var(--stage);
    font-family: "Exo 2", sans-serif;
    color: var(--ink);
    position: relative;
  }
  .card {
    position: absolute;
    left: 250px;
    width: 700px;
    height: 400px;
    background: radial-gradient(ellipse at 55% 40%, #ffffff 0%, var(--card) 55%, var(--card-edge) 100%);
    overflow: hidden;
  }
  .card--back { top: 35px; }
  .card--front { top: 465px; }

  .brand {
    position: absolute;
    display: flex;
    align-items: center;
    gap: 14px;
  }
  .brand__dot {
    border-radius: 50%;
    background: linear-gradient(160deg, var(--orange) 0%, var(--orange-deep) 100%);
    flex: none;
  }
  .brand__name {
    font-weight: 700;
    color: var(--ink);
    white-space: nowrap;
  }
  .card--back .brand { left: 200px; top: 150px; }
  .card--back .brand__dot { width: 100px; height: 100px; }
  .card--back .brand__name { font-size: 38px; }

  .card--front .brand { left: 350px; top: 112px; gap: 12px; }
  .card--front .brand__dot { width: 80px; height: 80px; }
  .card--front .brand__name { font-size: 28px; }

  .contact {
    position: absolute;
    left: 46px;
    top: 36px;
    font-size: 17px;
    letter-spacing: 1.5px;
    color: var(--ink-soft);
  }
  .contact__address { line-height: 25px; margin-bottom: 14px; }
  .contact__list { list-style: none; }
  .contact__item {
    display: flex;
    align-items: center;
    gap: 12px;
    height: 32px;
  }
  .contact__item svg { width: 18px; height: 18px; fill: var(--ink); flex: none; }
  .contact__item--email { font-size: 15px; letter-spacing: 0.5px; }

  .person {
    position: absolute;
    right: 40px;
    top: 250px;
    text-align: right;
    text-transform: uppercase;
  }
  .person__name { font-size: 23px; font-weight: 500; letter-spacing: 2px; }
  .person__role { font-size: 14px; font-weight: 500; letter-spacing: 2px; }

  .swoosh { position: absolute; left: 0; top: 0; width: 700px; height: 400px; }
</style>
</head>
<body>

<section class="card card--back" aria-label="Card back">
  <div class="brand">
    <span class="brand__dot"></span>
    <span class="brand__name">Melissa Dorvan</span>
  </div>
</section>

<section class="card card--front" aria-label="Card front">
  <svg class="swoosh" viewBox="0 0 700 400" aria-hidden="true">
    <defs>
      <linearGradient id="band" x1="0" y1="0" x2="1" y2="0">
        <stop offset="0" stop-color="#f28a1e"/>
        <stop offset="0.55" stop-color="#e0650f"/>
        <stop offset="1" stop-color="#f28a1e"/>
      </linearGradient>
    </defs>
    <path d="M0 275 C 200 270, 470 300, 700 400 L 700 400 L 0 400 Z" fill="url(#band)"/>
    <path d="M0 268 C 230 262, 480 300, 700 392" fill="none" stroke="var(--orange-light)" stroke-width="3"/>
    <path d="M0 250 C 250 252, 500 285, 700 370" fill="none" stroke="var(--rule)" stroke-width="4"/>
  </svg>

  <div class="contact">
    <p class="contact__address">5820 Halvers Lane #417<br>San Jose CA</p>
    <ul class="contact__list">
      <li class="contact__item">
        <svg viewBox="0 0 24 24"><path d="M6.6 10.8a15.1 15.1 0 0 0 6.6 6.6l2.2-2.2c.3-.3.7-.4 1-.2 1.1.4 2.3.6 3.6.6.6 0 1 .4 1 1V20c0 .6-.4 1-1 1A17 17 0 0 1 3 4c0-.6.4-1 1-1h3.5c.6 0 1 .4 1 1 0 1.3.2 2.5.6 3.6.1.3 0 .7-.2 1z"/></svg>
        <span>408 517 2049</span>
      </li>
      <li class="contact__item">
        <svg viewBox="0 0 24 24"><path d="M7 1h10a2 2 0 0 1 2 2v18a2 2 0 0 1-2 2H7a2 2 0 0 1-2-2V3a2 2 0 0 1 2-2zm0 3v14h10V4zm5 15.5a1.2 1.2 0 1 0 0 2.4 1.2 1.2 0 0 0 0-2.4z"/></svg>
        <span>408 517 2049</span>
      </li>
      <li class="contact__item">
        <svg viewBox="0 0 24 24"><path d="M7 2h9v5H7zM3 8h18v13H3zm3 3v2h3v-2zm5 0v2h3v-2zm5 0v2h2v-2zM6 15v2h3v-2zm5 0v2h3v-2z"/></svg>
        <span>408 517 2049</span>
      </li>
      <li class="contact__item contact__item--email">
        <svg viewBox="0 0 24 24"><path d="M2 5h20v14H2zm2 2v.5l8 5.5 8-5.5V7zm0 3v7h16v-7l-8 5.5z"/></svg>
        <span>hello@dorvanmail.com</span>
      </li>
    </ul>
  </div>

  <div class="brand">
    <span class="brand__dot"></span>
    <span class="brand__name">Melissa Dorvan</span>
  </div>

  <div class="person">
    <p class="person__name">Daniel Mercer</p>
    <p class="person__role">Financial Advisor</p>
  </div>
</section>

</body>
</html>
```